Pale Lantern Double Sided Flyer Design

We need a double sided flyer (1/3 of an A4 which is 99mm x 210mm) developed for our Newcastle(NSW) tour. This flyer will be placed in tourist information centres and hotels. We want it to direct people to our website or be able to make bookings over the phone.

About Us:-
We are a city walking tour company that runs tours day or night. We run both day and night and will incorporate real history / real Pale lantern. Some of the stories will be quite serious i.e.- there are infamous murders from 100 years ago, baffling court cases, even a bit of poetry written by murderers, suicides, love triangles, you name it. We will be telling the historical stories that tourists will not hear from any other tour provider. A bit of darkness, a bit of mystery and a bit of history theme.

We do no go for scares and let the very real stories deliver the entertainment for our guests. Our customers enjoy our tours, but it isn't light fun and frivolity. Our stories are being carefully crafted and are packed with unexpected twists, turns; revelations whilst remaining all 100% true. We deliver deep, rich, engaging stories.

Here are a few samples of quotes from the characters in our stories that may give you an idea of the kind of history we will cover:-

"There were bits of spines, bits of skulls, [and] finger bones spilled out all over the streets - I ended up filling three boxes. Children were playing with them for weeks”

"I had a close shave last night and now I want a close haircut.”

“She's a beautiful child', isn't she? She's the cause of all the trouble.”

“I did it because she would not come home with me.”

"I have killed my wife. I’m glad she’s dead.”

"Stand aside or I'll put a bullet through both of you."

“You villain, I'll teach you to take away my character."

“You’re not dead yet, you bastard!”

Our website, booking form and contact details can be viewed at www.palelantern.com.au

Target Market(s)

Tourists

Industry/Entity Type

Tour

Colors

Designer to choose colors to be used in the design.

Requirements
Must have
• Vertical orientation please.
• Please also include a reference to a discount offer of 25% using the promo code "WICK".
Nice to have
• FRONT FLYER INFORMATION
• - Pale Lantern Logo
• - "I have killed my wife; I'm glad she's dead."
• - Harbourside Hidden Lanes Walk
• - 25% Discount Offer Codeword WICK
• - web address at the base; www.palelantern.com.au
• BACK FLYER INFORMATION
• - "She's a beautiful child', isn't she? She's the cause of all the trouble.
• - Pale Lantern Logo at the base along with the web address www.palelantern.com.au
• - Blurb:- Pale lantern brings back Newcastle's hidden past, the forgotten past, the dark past that may not want to be remembered.
• Real stories from the streets around you. Discover the histories you won't hear anywhere else. The forgotten stories of yesteryear finally get a chance to be told. Through you they get to live again.
Should not have
• GENERAL
• Please do not include the phone number, email address or social media icons. We want to drive online bookings.

```html
<!DOCTYPE html>
<html lang="en">
<head>
<meta charset="utf-8">
<title>Pale Lantern – Flyer Back</title>
<link href="https://fonts.googleapis.com/css2?family=DM+Serif+Display&family=Work+Sans:wght@400&display=swap" rel="stylesheet">
<style>
  :root {
    --blood-red: #ce2129;
    --paper: #ffffff;
    --tear-shadow: #b9b9b9;
    --print-dark: #3b0c0e;
    --print-light: #dc5a4d;
    --ink: #1d1d1d;
  }
  html, body {
    margin: 0;
    padding: 0;
    width: 1200px;
    height: 2546px;
    overflow: hidden;
    background: var(--paper);
  }
  .flyer {
    position: relative;
    width: 1200px;
    height: 2546px;
    overflow: hidden;
    background: var(--paper);
  }
  .torn-panel, .footprints {
    position: absolute;
    inset: 0;
    width: 1200px;
    height: 2546px;
  }
  .torn-panel .red-field { fill: var(--blood-red); }
  .torn-panel .tear-edge { fill: var(--tear-shadow); }
  .quote {
    position: absolute;
    left: 122px;
    top: 92px;
    width: 960px;
    margin: 0;
    font-family: "DM Serif Display", Georgia, serif;
    font-weight: 400;
    font-size: 94px;
    line-height: 110px;
    letter-spacing: -1.5px;
    color: var(--paper);
    white-space: nowrap;
  }
  .quote span { display: block; }
  .quote .right { text-align: right; }
  .blurb {
    position: absolute;
    left: 150px;
    top: 1912px;
    width: 900px;
    font-family: "Work Sans", Arial, sans-serif;
    font-weight: 400;
    font-size: 33px;
    line-height: 46px;
    color: var(--ink);
    text-align: center;
  }
  .blurb p { margin: 0 0 46px; }
  .sign-off {
    position: absolute;
    left: 0;
    top: 2352px;
    width: 1200px;
    text-align: center;
    color: var(--ink);
  }
  .brand-name {
    display: inline-flex;
    align-items: center;
    gap: 16px;
    font-family: "DM Serif Display", Georgia, serif;
    font-size: 48px;
    line-height: 56px;
    color: var(--blood-red);
  }
  .brand-mark {
    width: 22px;
    height: 22px;
    border-radius: 50%;
    background: var(--blood-red);
  }
  .web-address, .promo {
    font-family: "Work Sans", Arial, sans-serif;
    font-size: 28px;
    line-height: 40px;
    margin: 6px 0 0;
  }
  .promo strong { color: var(--blood-red); font-weight: 400; }
</style>
</head>
<body>
<main class="flyer">
  <svg class="torn-panel" viewBox="0 0 1200 2546" aria-hidden="true">
    <polygon class="tear-edge" points="0,886 60,890 130,884 210,900 300,915 380,930 470,950 560,975 660,1000 740,1012 748,1022 760,1016 850,1040 950,1062 1050,1080 1130,1095 1200,1110 1200,1132 1120,1118 1020,1102 920,1082 820,1062 740,1036 640,1020 540,996 440,972 340,950 240,930 140,912 60,904 0,900"/>
    <polygon class="red-field" points="0,0 1200,0 1200,1106 1130,1090 1050,1074 950,1056 850,1034 760,1010 748,1018 740,1006 660,994 560,968 470,944 380,924 300,909 210,894 130,878 60,884 0,880"/>
  </svg>

  <svg class="footprints" viewBox="0 0 1200 2546">
    <defs>
      <radialGradient id="print-dark-glow">
        <stop offset="0" stop-color="#3b0c0e" stop-opacity="0.75"/>
        <stop offset="1" stop-color="#3b0c0e" stop-opacity="0"/>
      </radialGradient>
      <radialGradient id="print-light-glow">
        <stop offset="0" stop-color="#dc5a4d" stop-opacity="0.7"/>
        <stop offset="1" stop-color="#dc5a4d" stop-opacity="0"/>
      </radialGradient>
    </defs>
    <g role="img" aria-label="Trail of dark inked baby footprints walking across the red field">
      <rect x="1000" y="90" width="200" height="230" fill="url(#print-dark-glow)"/>
      <rect x="910" y="530" width="210" height="220" fill="url(#print-dark-glow)"/>
      <rect x="550" y="660" width="210" height="230" fill="url(#print-dark-glow)"/>
    </g>
    <g role="img" aria-label="Trail of red inked baby footprints continuing across the white paper">
      <rect x="620" y="1080" width="220" height="220" fill="url(#print-light-glow)"/>
      <rect x="230" y="1150" width="200" height="230" fill="url(#print-light-glow)"/>
      <rect x="240" y="1540" width="200" height="230" fill="url(#print-light-glow)"/>
      <rect x="-80" y="1580" width="190" height="230" fill="url(#print-light-glow)"/>
    </g>
  </svg>

  <h1 class="quote">
    <span>"She's a beautiful child',</span>
    <span>isn't she?</span>
    <span class="right">She's the cause of</span>
    <span class="right">all the trouble.</span>
  </h1>

  <section class="blurb">
    <p>Pale lantern brings back Newcastle's<br>hidden past, the forgotten past, the dark<br>past that may not want to be remembered.</p>
    <p>Real stories from the streets around you.<br>Discover the histories you won't hear<br>anywhere else. The forgotten stories of<br>yesteryear finally get a chance to be told.<br>Through you they get to live again.</p>
  </section>

  <footer class="sign-off">
    <div class="brand-name"><span class="brand-mark"></span>Pale Lantern</div>
    <p class="web-address">www.palelantern.com.au</p>
    <p class="promo">Book online – 25% off with code <strong>WICK</strong></p>
  </footer>
</main>
</body>
</html>
```